Flyer Design Project for our Parenting Psychologists at the Wellmind Counselling Centre

At the Wellmind Counselling Centre we have expert Parenting Psychologists.

Parenting Psychologists provide practical, step by step assistance to parents who are struggling with their children's behavioural and emotional problems.

We need a DL size brochure that will be appealing to parents. The brochure will be on show in schools, kindergartens and GP clinics.

In terms of style it will be in line with our website and stationery that I will attach.

www.wellmindcounsellingcentre.com.au

Hi Everyone,
Thanks for putting forward your proposals, there are a couple there that I am very interested in. I am looking to see if there is a way that I can change my brief to guaranteed as I am definitely going to be using one of the designs for sure.
I have emailed ArtForge and as soon as I get an answer I will change it if I can.
If anyone out there already knows the answer please let me know :-)
Thanks,
Marcie.

Hi Again,

I worked it out myself!!

I have now changed this to a committed project.

Kind regards,
Marcie.

Reason: I have 46 designs now and need more time to work out which is best!

Target Market(s)

The target will be educated professional parents motivated to get professional help. And doctors and teachers who will pass on the brochures 2 parents

Industry/Entity Type

Health

Requirements
Must have
• I want one DL size brochure. Back and front.

We need text (below) and our contact details. Our logo.

6352 1840
Suite 1, 2087 Tamworth Rd, Tamworth North 3118

Text:
Parents want the best for their kids. They want kids that are happy, healthy and well behaved.

So why is it so hard? Parents of toddlers, primary schoolers and teenagers alike say that they are frustrated by constant nagging, bribing and yelling, they don't know what to try next. Some parents worry that their children are unhappy. Struggling at school, not making friends or coping with bigger problems.

The good news is that getting your children to behave more co-operatively doesn't need to be difficult or mysterious. We all know that kids don't come with manuals, but there are skills every parent can learn to make parenting easier. In a few sessions with a Parenting Psychologist, you will receive step by step guidance in how to talk to your children in a way that will be much more effective getting them to behave in a respectful and co-operative way around the home and in public. You will learn how to help your child cope with problems they are going through. They can help you reconnect with your kids so you can enjoy being a parent again.

Nice to have
• Themes consistent with our website
and letterhead, business cards. I will attach these.
Should not have
• I don't want it to look too cluttered so if the text I have provided up above looks too crowded then I will edit it.

```html
<!DOCTYPE html>
<html lang="en">
<head>
<meta charset="utf-8">
<title>Wellmind Counselling Centre – Parenting Advice DL Flyer</title>
<link href="https://fonts.googleapis.com/css2?family=Lato:ital,wght@1,900&family=Open+Sans:ital,wght@0,400;0,600;0,700;1,400;1,600&family=Yanone+Kaffeesatz:wght@400;500&display=swap" rel="stylesheet">
<style>
  :root {
    --green: #5b9476;
    --teal: #6bbcc4;
    --steel: #5f93a0;
    --slate: #6f828f;
    --deep-teal: #3e6a72;
    --charcoal: #3d3d3d;
    --olive: #8d9479;
    --heading-teal: #3d6670;
    --grey-text: #555a5c;
    --body-text: #4a4a4a;
    --magenta: #d4237a;
    --orange: #f07f1f;
    --paper: #ffffff;
    --page-bg: #e4e6e6;
  }
  * { box-sizing: border-box; margin: 0; padding: 0; }
  html, body { width: 1200px; height: 1122px; overflow: hidden; }
  body {
    background: var(--page-bg);
    font-family: "Open Sans", Arial, sans-serif;
    position: relative;
  }
  .panel {
    position: absolute;
    top: 89px;
    width: 442px;
    height: 943px;
    background: linear-gradient(180deg, #ffffff 0%, #f7f7f7 45%, #eeeeee 100%);
    overflow: hidden;
    box-shadow: 0 2px 10px rgba(0,0,0,0.12);
  }
  .panel--front { left: 120px; }
  .panel--back { left: 633px; }

  .stripe { position: absolute; left: 0; width: 100%; height: 10px; display: flex; }
  .stripe span { flex: 1; }
  .stripe span:nth-child(8n+1) { background: var(--green); }
  .stripe span:nth-child(8n+2) { background: var(--teal); }
  .stripe span:nth-child(8n+3) { background: var(--steel); }
  .stripe span:nth-child(8n+4) { background: var(--slate); }
  .stripe span:nth-child(8n+5) { background: var(--deep-teal); }
  .stripe span:nth-child(8n+6) { background: var(--teal); }
  .stripe span:nth-child(8n+7) { background: var(--charcoal); }
  .stripe span:nth-child(8n+8) { background: var(--olive); }
  .stripe--top { top: 0; }

  .brand { position: absolute; display: flex; align-items: center; gap: 12px; }
  .brand__dot { width: 44px; height: 44px; border-radius: 50%; background: var(--teal); flex: none; }
  .brand__name {
    font-family: "Open Sans", Arial, sans-serif;
    font-weight: 400;
    font-size: 12.5px;
    line-height: 15px;
    letter-spacing: 2.2px;
    color: var(--slate);
    text-transform: uppercase;
  }

  /* Front panel */
  .front__brand { left: 20px; top: 38px; }
  .headline {
    position: absolute;
    right: 22px;
    top: 26px;
    text-align: right;
    font-family: "Yanone Kaffeesatz", "Arial Narrow", sans-serif;
    font-weight: 500;
    font-size: 84px;
    line-height: 94px;
  }
  .headline__expert { color: var(--green); }
  .headline__parenting { color: var(--heading-teal); }
  .headline__advice { color: var(--grey-text); }
  .age-range {
    position: absolute;
    right: 22px;
    top: 320px;
    text-align: right;
    font-style: italic;
    font-weight: 600;
    font-size: 24px;
    line-height: 32px;
    color: var(--grey-text);
  }
  .thought-dots { position: absolute; left: 276px; top: 404px; }
  .family-photo {
    position: absolute;
    left: 0;
    top: 270px;
    width: 305px;
    height: 575px;
    background: radial-gradient(ellipse at 50% 55%, #e6c4a8 0%, #d8b08f 35%, #c89e82 60%, rgba(235,228,220,0.6) 85%, rgba(255,255,255,0) 100%);
  }
  .wish-bubble { position: absolute; right: 0; top: 450px; width: 112px; height: 218px; }
  .wish-bubble__text {
    position: absolute;
    right: 16px;
    top: 474px;
    text-align: right;
    font-family: "Yanone Kaffeesatz", "Arial Narrow", sans-serif;
    font-weight: 400;
    font-size: 23px;
    line-height: 28px;
    color: var(--paper);
  }
  .availability {
    position: absolute;
    right: 0;
    top: 740px;
    width: 204px;
    height: 103px;
    background: var(--paper);
  }
  .availability .stripe { top: 0; height: 14px; }
  .availability__icon { position: absolute; right: 14px; top: -22px; width: 48px; height: 48px; }
  .availability__title {
    position: absolute;
    right: 12px;
    top: 28px;
    font-family: "Yanone Kaffeesatz", "Arial Narrow", sans-serif;
    font-weight: 500;
    font-size: 33px;
    line-height: 36px;
    color: var(--heading-teal);
    white-space: nowrap;
  }
  .availability__sub {
    position: absolute;
    right: 12px;
    top: 68px;
    font-weight: 600;
    font-size: 14px;
    color: var(--charcoal);
    white-space: nowrap;
  }
  .front__contact {
    position: absolute;
    left: 0;
    bottom: 0;
    width: 100%;
    height: 100px;
    background: var(--teal);
    text-align: center;
    padding-top: 12px;
  }
  .call-line {
    font-weight: 700;
    font-size: 39px;
    line-height: 46px;
    color: var(--charcoal);
  }
  .front__web { font-size: 18px; color: #4d5a5e; line-height: 24px; }

  /* Back panel */
  .back__title {
    position: absolute;
    left: 24px;
    top: 20px;
    font-family: "Lato", Arial, sans-serif;
    font-style: italic;
    font-weight: 900;
    font-size: 32px;
    color: var(--magenta);
  }
  .back__intro {
    position: absolute;
    left: 24px;
    top: 76px;
    width: 246px;
    font-style: italic;
    font-size: 15.3px;
    line-height: 21.8px;
    color: var(--grey-text);
  }
  .child-photo-frame { position: absolute; left: 258px; top: 76px; width: 200px; height: 220px; }
  .back__body {
    position: absolute;
    left: 24px;
    top: 312px;
    width: 395px;
    font-size: 15.3px;
    line-height: 21.6px;
    color: var(--body-text);
    text-align: justify;
  }
  .back__body strong { color: var(--orange); font-weight: 700; }
  .kids-photo {
    position: absolute;
    left: 0;
    top: 598px;
    width: 100%;
    height: 202px;
    background: linear-gradient(180deg, rgba(240,240,240,0) 0%, #f0d6c3 30%, #e3a98c 60%, #d9683c 85%, #c84a34 100%);
  }
  .back__footer {
    position: absolute;
    left: 0;
    top: 800px;
    width: 100%;
    height: 143px;
    background: var(--paper);
  }
  .back__footer .stripe--mid { top: 0; height: 9px; }
  .back__footer .stripe--bottom { bottom: 0; }
  .back__brand { left: 20px; top: 24px; }
  .back__address {
    position: absolute;
    right: 18px;
    top: 22px;
    text-align: right;
    font-size: 11.5px;
    line-height: 16px;
    color: var(--charcoal);
  }
  .back__call { position: absolute; left: 0; width: 100%; top: 72px; text-align: center; font-size: 40px; }
</style>
</head>
<body>

<section class="panel panel--front" aria-label="Flyer front">
  <div class="stripe stripe--top"><span></span><span></span><span></span><span></span><span></span><span></span><span></span><span></span></div>

  <div class="brand front__brand">
    <span class="brand__dot"></span>
    <span class="brand__name">Wellmind<br>Counselling<br>Centre</span>
  </div>

  <h1 class="headline">
    <span class="headline__expert">Expert</span><br>
    <span class="headline__parenting">Parenting</span><br>
    <span class="headline__advice">Advice</span>
  </h1>

  <p class="age-range">From toddlers<br>to teens</p>

  <div class="family-photo" role="img" aria-label="Photo of a smiling family: mother, father and three children piled together"></div>

  <svg class="thought-dots" width="120" height="30" viewBox="0 0 120 30" aria-hidden="true">
    <ellipse cx="8" cy="20" rx="7" ry="4.5" fill="#6bbcc4"/>
    <ellipse cx="40" cy="16" rx="13" ry="7.5" fill="#6bbcc4"/>
    <ellipse cx="90" cy="13" rx="23" ry="12" fill="#6bbcc4"/>
  </svg>

  <svg class="wish-bubble" viewBox="0 0 112 218" aria-hidden="true">
    <g fill="#6bbcc4">
      <rect x="45" y="8" width="67" height="206"/>
      <circle cx="68" cy="36" r="34"/>
      <circle cx="34" cy="82" r="32"/>
      <circle cx="30" cy="132" r="30"/>
      <circle cx="44" cy="178" r="36"/>
    </g>
  </svg>
  <p class="wish-bubble__text">We want<br>kids who<br>are happy,<br>health<br>and well<br>behaved</p>

  <div class="availability">
    <div class="stripe"><span></span><span></span><span></span><span></span><span></span><span></span><span></span><span></span></div>
    <svg class="availability__icon" viewBox="0 0 48 48" aria-hidden="true">
      <circle cx="24" cy="24" r="22" fill="#ffffff" stroke="#3e6a72" stroke-width="3"/>
      <circle cx="24" cy="24" r="12" fill="none" stroke="#3e6a72" stroke-width="2.5"/>
      <path d="M24 16 V24 H30" fill="none" stroke="#3e6a72" stroke-width="2.5" stroke-linecap="round"/>
    </svg>
    <p class="availability__title">No Waiting Lists</p>
    <p class="availability__sub">After hours Appointments</p>
  </div>

  <div class="front__contact">
    <p class="call-line">Call on 6352 1840</p>
    <p class="front__web">www.wellmindcounsellingcentre.com.au</p>
  </div>
</section>

<section class="panel panel--back" aria-label="Flyer back">
  <div class="stripe stripe--top"><span></span><span></span><span></span><span></span><span></span><span></span><span></span><span></span></div>

  <h2 class="back__title">So why is it so hard?</h2>
  <p class="back__intro">Parents of toddlers, primary schoolers and teenagers alike say that they are frustrated by constant nagging, bribing and yelling, they don't know what to try next. Some parents worry that their children are dealing with big problems like depression, self-harm or an eating disorder.</p>

  <svg class="child-photo-frame" viewBox="0 0 200 220" aria-hidden="true">
    <circle cx="110" cy="106" r="104" fill="#f1f1f1"/>
    <circle cx="110" cy="106" r="94" fill="#ffffff"/>
  </svg>
  <div role="img" aria-label="Photo of a defiant little boy with hands on hips while an adult points at him" style="position:absolute;left:282px;top:96px;width:176px;height:176px;border-radius:50%;background:radial-gradient(circle at 55% 45%, #e5c2a4 0%, #b89a7e 45%, #8b8f96 75%, #f4f4f4 100%);"></div>

  <p class="back__body"><strong>The good news</strong> is that parenting doesn't need to be difficult or mysterious. We all know that kids don't come with manuals, but there are skills every parent can learn to make parenting easier. In a few sessions with a Parenting Psychologist, you will receive step by step guidance in how to talk to your children in a way that will be much more effective getting them to behave in a respectful and co-operative way. You will learn how to help your child cope with problems they are going through. They can help you reconnect with your kids so you can enjoy being a parent again.</p>

  <div class="kids-photo" role="img" aria-label="Photo of four smiling children lying side by side, chins resting on their hands"></div>

  <div class="back__footer">
    <div class="stripe stripe--mid"><span></span><span></span><span></span><span></span><span></span><span></span><span></span><span></span><span></span><span></span></div>
    <div class="brand back__brand">
      <span class="brand__dot"></span>
      <span class="brand__name">Wellmind<br>Counselling<br>Centre</span>
    </div>
    <p class="back__address">Suite 1, 2087 Tamworth Rd,<br>Tamworth North 3118<br>www.wellmindcounsellingcentre.com.au</p>
    <p class="call-line back__call">Call on 6352 1840</p>
    <div class="stripe stripe--bottom"><span></span><span></span><span></span><span></span><span></span><span></span><span></span><span></span><span></span><span></span></div>
  </div>
</section>

</body>
</html>
```